Vireo Kinetics LLC Sports Therapy and Soft Tissue Injury solutions

We are a company that specializes in Sports Therapy, Physical therapy, muscular rehab, nutrition plans, and personal training. Vireo Kinetics travels around the country and world treating athletes and people in the workforce that have Soft Tissue injuries. We are legally partnered with QMD(Fluent Motion Protocols/fluentmotion.example) in treating endurance athletes ex. SteelWave triathalon. We educate our patients on how to sustain a healthy lifestyle.We need a web design that has a Home page summarizing our services, a Physical therapy page, a Personal training and nutrition page. Our ultimate goal is to build relationships with fitness centers, training facilities, and companies that are implementing preventative health measures for their employees. We want to incorporate the QMD logo and Steelwave logo attached in the website but, we want to use our own name (Vireo Kinetics LLC) as the main draw. We will provide literature for the website.

Target Market(s)

Brisk rig training gyms, Fitness centers, Dance studios, Companies looking for Corporate Wellness programs

Industry/Entity Type

Health And Wellness

Number of Pages Required

4 page

Font styles to use
Sans Serif

Requirements
Must have
• Stock Photos of Athletes training. Examples of Endurance Athletes and Cross training. A mesh of as many sports and training methods as possible. We are a new company and don't have many photos. Easy accessibility to change and add text as the company grows. Fluent Motion protocols logo incorporated in the back ground of the website. Always visible but does not take over the web page
Nice to have
• Sleek and cool, and masculine design. We want the website to stand out without focusing on one individual. We want to use the website to brand the company (Vireo Kinetics LLC) with easy access to social media platforms

```html
<!DOCTYPE html>
<html lang="en">
<head>
<meta charset="utf-8">
<title>Vireo Kinetics LLC</title>
<link href="https://fonts.googleapis.com/css2?family=Montserrat:wght@400;600;700&family=Open+Sans:ital,wght@0,400;0,600;1,400&display=swap" rel="stylesheet">
<style>
:root{
  --orange:#ff7f00;
  --ink:#3a3a3a;
  --muted:#8a8a8a;
  --line:#e2e2e2;
  --footer:#f3f3f3;
  --white:#ffffff;
  --dark:#1f1f1f;
}
*{margin:0;padding:0;box-sizing:border-box}
html,body{width:1200px;height:2247px;overflow:hidden;background:var(--white)}
body{position:relative;font-family:"Open Sans",Arial,sans-serif;color:var(--ink)}
.abs{position:absolute}
.heading{font-family:"Montserrat",Arial,sans-serif;font-weight:700;text-transform:uppercase}

/* header */
.site-header{left:0;top:0;width:1200px;height:86px;background:var(--white)}
.brand{left:131px;top:26px;font-family:"Montserrat",Arial,sans-serif;font-weight:700;font-size:27px;color:var(--orange)}
.main-nav{left:467px;top:0;display:flex;height:86px}
.main-nav a{display:flex;align-items:center;padding:0 16px;font-family:"Montserrat",Arial,sans-serif;font-size:11.5px;font-weight:600;color:var(--ink);text-decoration:none;text-transform:uppercase}
.main-nav a.active{background:var(--orange);color:var(--white);padding:0 17px}

/* hero */
.hero{left:0;top:86px;width:1200px;height:531px;background:linear-gradient(180deg,#2f5fa0 0%,#5d86b5 28%,#7a9a62 48%,#8aa63e 62%,#a55d4a 78%,#9a4a3c 100%)}
.hero-title{right:132px;top:257px;background:rgba(25,25,25,.88);color:var(--white);font-size:29px;padding:15px 16px;letter-spacing:.3px}
.hero-text{right:132px;top:334px;width:400px;text-align:right;color:var(--white);font-size:14px;font-weight:600;line-height:27px}
.btn{background:var(--orange);color:var(--white);font-family:"Montserrat",Arial,sans-serif;font-weight:600;text-transform:uppercase;text-align:center}
.hero-btn{right:132px;top:409px;width:178px;height:39px;line-height:39px;font-size:12px}
.slide-arrow{top:330px;width:45px;height:45px;border-radius:50%;background:rgba(40,40,40,.65)}
.slide-arrow svg{display:block;margin:15px auto}

/* welcome */
.welcome-title{left:0;top:666px;width:1200px;text-align:center;font-size:24px;color:var(--ink)}
.welcome-text{left:190px;top:709px;width:820px;text-align:center;font-size:11.5px;line-height:22px;color:var(--muted)}
.feature{top:812px;width:310px;display:flex;gap:18px}
.feature-icon{flex:none;width:76px;height:76px;border-radius:50%;background:var(--orange);border:3px solid #ffd1a3;display:flex;align-items:center;justify-content:center}
.feature h3{font-size:12.5px;font-weight:600;color:var(--ink);margin-top:3px;margin-bottom:4px}
.feature p{font-size:11.5px;line-height:19.5px;color:var(--muted)}

/* services */
.services-band{left:0;top:0}
.services-title{left:0;top:1038px;width:1200px;text-align:center;color:var(--white);font-size:30px}
.service-card{top:1112px;width:224px;height:325px;background:var(--white);box-shadow:0 2px 6px rgba(0,0,0,.25);text-align:center}
.service-photo{margin:7px 7px 0;height:150px}
.service-card h3{font-family:"Montserrat",Arial,sans-serif;font-size:12.5px;font-weight:700;color:var(--ink);margin-top:20px}
.service-card p{font-size:11.5px;line-height:19.5px;color:var(--muted);margin:8px 18px 0}
.card-btn{display:inline-block;margin-top:15px;width:106px;height:30px;line-height:30px;font-size:10px}
.band-arrow{top:1163px}

/* testimonials */
.testimonials-title{left:0;top:1573px;width:1200px;text-align:center;font-size:23px;color:var(--ink)}
.avatar{left:135px;top:1615px;width:93px;height:93px;border-radius:50%;background:radial-gradient(circle at 50% 40%,#e7c3a8,#b7c2cc 70%)}
.testimonial-body{left:268px;top:1626px;width:812px}
.quote{font-style:italic;font-size:11px;letter-spacing:-.1px;line-height:25px;color:var(--muted);text-indent:32px}
.quote-mark{font-family:Georgia,serif;font-size:44px;color:#c4c4c4;line-height:1}
.quote-open{left:0;top:-4px}
.quote-close{left:690px;top:40px}
.quote-author{margin-top:12px;font-size:11.5px;color:var(--orange)}
.dots{left:1014px;top:1706px;display:flex;gap:9px}
.dots span{width:6px;height:6px;border-radius:50%;background:#bdbdbd}
.dots span.on{background:var(--orange)}

/* partners */
.partner{top:1772px;width:458px;height:105px;border:1px solid var(--line);display:flex;align-items:center}
.partner-name{width:200px;display:flex;align-items:center;justify-content:center;gap:10px;font-family:"Montserrat",Arial,sans-serif;font-weight:700;font-size:26px;color:#555}
.partner-name i{width:16px;height:16px;background:#555;display:block}
.partner p{font-size:11.5px;line-height:22.5px;color:var(--muted);width:236px;margin-left:12px}

/* footer */
.site-footer{left:0;top:1946px;width:1200px;height:251px;background:var(--footer)}
.footer-col h4{font-family:"Montserrat",Arial,sans-serif;font-size:13px;font-weight:600;color:var(--ink);text-transform:uppercase;margin-bottom:18px}
.footer-divider{top:1990px;width:1px;height:165px;background:#dcdcdc}
.contact-row{display:flex;gap:12px;font-size:11.5px;color:#555;line-height:19px;margin-bottom:14px}
.contact-row svg{flex:none;margin-top:2px}
.newsletter p{font-size:11px;color:#555;line-height:18px;margin-bottom:10px}
.field{width:246px;height:37px;background:var(--white);border:1px solid var(--line);font-size:11px;color:var(--muted);line-height:37px;padding-left:12px;margin-bottom:12px;position:relative}
.subscribe{position:absolute;right:-1px;top:-1px;width:92px;height:37px;line-height:37px;font-size:11px}
.links li{list-style:none;font-size:11px;color:#555;line-height:24px;display:flex;align-items:center;gap:12px}
.links li::before{content:"";border-left:4px solid #555;border-top:3px solid transparent;border-bottom:3px solid transparent}
.social li{list-style:none;display:flex;align-items:center;gap:12px;font-size:11px;color:#555;margin-bottom:7px}
.social li span{width:28px;height:28px;border-radius:50%;background:var(--white);box-shadow:0 1px 3px rgba(0,0,0,.12);display:flex;align-items:center;justify-content:center}
.social li span i{width:8px;height:8px;border-radius:50%;background:var(--orange);display:block}
.copyright{left:0;top:2214px;width:1200px;text-align:center;font-size:11px;color:var(--ink)}
</style>
</head>
<body>

<header class="site-header abs">
  <div class="brand abs">VIREO KINETICS <span style="color:var(--dark)">LLC</span></div>
  <nav class="main-nav abs">
    <a class="active" href="#">Home</a>
    <a href="#">Services</a>
    <a href="#">Physical Therapy</a>
    <a href="#">Personal Training</a>
    <a href="#">Nutrition</a>
    <a href="#">Contact Us</a>
  </nav>
</header>

<section class="hero abs" role="img" aria-label="Sprinter launching from starting blocks on a stadium track"></section>
<div class="slide-arrow abs" style="left:46px"><svg width="10" height="14" viewBox="0 0 10 14"><path d="M8 1 2 7l6 6" fill="none" stroke="#fff" stroke-width="2.5"/></svg></div>
<div class="slide-arrow abs" style="left:1108px"><svg width="10" height="14" viewBox="0 0 10 14"><path d="M2 1l6 6-6 6" fill="none" stroke="#fff" stroke-width="2.5"/></svg></div>
<h1 class="hero-title heading abs">Soft Tissue Injuries</h1>
<p class="hero-text abs">Nemo enim ipsam voluptatem quia voluptas sit aspernatur aut odit aut fugit, sed quia consequuntur...</p>
<div class="hero-btn btn abs">View More Information</div>

<h2 class="welcome-title heading abs">Welcome Vireo Kinetics LLC</h2>
<p class="welcome-text abs">Numquam eius modi tempora incidunt ut labore et dolore magnam aliquam quaerat voluptatem. Ut enim ad minima veniam, quis nostrum exercitationem ullam corporis suscipit laboriosam, nisi ut aliquid ex ea commodi consequatur? Quis autem vel eum iure reprehenderitsoluta nobis est eligendi optio cumque nihil impedit quo minus id quod voluptas assumenda est, omnis..,</p>

<div class="feature abs" style="left:131px">
  <div class="feature-icon"><svg width="44" height="24" viewBox="0 0 44 24" fill="none" stroke="#fff" stroke-width="2"><rect x="6" y="3" width="6" height="18" rx="1"/><rect x="32" y="3" width="6" height="18" rx="1"/><rect x="1" y="7" width="5" height="10" rx="1"/><rect x="38" y="7" width="5" height="10" rx="1"/><path d="M12 12h20"/></svg></div>
  <div><h3>Cum Soluta Nobis</h3><p>Sunt in culpa qui officia deserunt molli animi, id est laborum et dolorum fuga. Et harum quidem rerum...</p></div>
</div>
<div class="feature abs" style="left:460px">
  <div class="feature-icon"><svg width="44" height="30" viewBox="0 0 44 30" fill="none" stroke="#fff" stroke-width="2"><circle cx="10" cy="7" r="4"/><path d="M4 22h36M8 26h30M14 14l10 4h10"/><circle cx="36" cy="18" r="4"/></svg></div>
  <div><h3>Cum Soluta Nobis</h3><p>Sunt in culpa qui officia deserunt molli animi, id est laborum et dolorum fuga. Et harum quidem rerum...</p></div>
</div>
<div class="feature abs" style="left:790px">
  <div class="feature-icon"><svg width="40" height="40" viewBox="0 0 40 40" fill="none" stroke="#fff" stroke-width="2"><path d="M10 14l8 6-6 16-6-16z"/><path d="M10 14l-2-8M12 14l4-7"/><circle cx="28" cy="27" r="9"/><path d="M28 18v-4"/></svg></div>
  <div><h3>Cum Soluta Nobis</h3><p>Sunt in culpa qui officia deserunt molli animi, id est laborum et dolorum fuga. Et harum quidem rerum...</p></div>
</div>

<svg class="services-band abs" width="1200" height="2247" viewBox="0 0 1200 2247">
  <polygon points="0,932 600,982 1200,932 1200,1555 600,1504 0,1555" fill="#ff7f00"/>
</svg>
<h2 class="services-title heading abs">Our Services</h2>
<svg class="band-arrow abs" style="left:92px" width="14" height="62" viewBox="0 0 14 62"><path d="M13 1 1 31l12 30" fill="none" stroke="#fff" stroke-width="1.5"/></svg>
<svg class="band-arrow abs" style="left:1094px" width="14" height="62" viewBox="0 0 14 62"><path d="M1 1l12 30L1 61" fill="none" stroke="#fff" stroke-width="1.5"/></svg>

<article class="service-card abs" style="left:132px">
  <div class="service-photo" role="img" aria-label="Runner's foot on a treadmill" style="background:linear-gradient(135deg,#3b3f48,#9a8f86 60%,#d07a3a)"></div>
  <h3>SPORTS THERAPY</h3><p>Circumstances occur in which toil and pain can procure him some great pleasure...</p>
  <div class="card-btn btn">Read More Info</div>
</article>
<article class="service-card abs" style="left:370px">
  <div class="service-photo" role="img" aria-label="Therapist stretching a patient's leg" style="background:linear-gradient(135deg,#6c6a68,#b9aca0 55%,#d9d3cb)"></div>
  <h3>PHYSICAL THERAPY</h3><p>Circumstances occur in which toil and pain can procure him some great pleasure...</p>
  <div class="card-btn btn">Read More Info</div>
</article>
<article class="service-card abs" style="left:607px">
  <div class="service-photo" role="img" aria-label="Massage of a leg muscle" style="background:linear-gradient(135deg,#7a4a38,#c8957a 55%,#e1bba4)"></div>
  <h3>MUSCULAR REHAB</h3><p>Circumstances occur in which toil and pain can procure him some great pleasure...</p>
  <div class="card-btn btn">Read More Info</div>
</article>
<article class="service-card abs" style="left:845px">
  <div class="service-photo" role="img" aria-label="Fresh vegetables beside a notepad on a wooden table" style="background:linear-gradient(135deg,#8a5a3a,#b9442f 35%,#a47a52 60%,#d8c3a4)"></div>
  <h3>NUTRITION PLANS</h3><p>Circumstances occur in which toil and pain can procure him some great pleasure...</p>
  <div class="card-btn btn">Read More Info</div>
</article>

<h2 class="testimonials-title heading abs">Testimonials</h2>
<div class="avatar abs" role="img" aria-label="Portrait of client Martin Hale"></div>
<div class="testimonial-body abs">
  <span class="quote-mark quote-open abs">&ldquo;</span>
  <p class="quote">Sed ut perspiciatis unde omnis iste natus error sit voluptatem accusantium doloremque laudantium, totam rem aperiam, eaque ipsa quae ab illo inventore veritatis et quasi architecto beatae vitae dicta sunt explicabo. Nemo enim ipsam voluptatem quia voluptas voluptatem sequi nesciunt....</p>
  <span class="quote-mark quote-close abs">&rdquo;</span>
  <div class="quote-author">-Martin Hale</div>
</div>
<div class="dots abs"><span></span><span class="on"></span><span></span><span></span></div>

<div class="partner abs" style="left:132px">
  <div class="partner-name"><i></i>QMD</div>
  <p>Account of the system, and expound actual teachings of the great explorer of the truth, the master-builder of human...</p>
</div>
<div class="partner abs" style="left:610px">
  <div class="partner-name">STEELWAVE</div>
  <p>Account of the system, and expound actual teachings of the great explorer of the truth, the master-builder of human...</p>
</div>

<footer class="site-footer abs"></footer>
<div class="footer-col abs" style="left:131px;top:1987px;width:230px">
  <h4>Contact Us</h4>
  <div class="contact-row"><svg width="12" height="16" viewBox="0 0 12 16"><path d="M6 0a6 6 0 0 1 6 6c0 4-6 10-6 10S0 10 0 6a6 6 0 0 1 6-6z" fill="#ff7f00"/><circle cx="6" cy="6" r="2.2" fill="#f3f3f3"/></svg><span>Vireo Kinetics LLC P.O. Box 4120<br>Street NAme,City-454</span></div>
  <div class="contact-row" style="font-size:14px"><svg width="13" height="13" viewBox="0 0 13 13"><path d="M2 0h3l1 3-2 1.5a8 8 0 0 0 4.5 4.5L10 7l3 1v3a2 2 0 0 1-2 2A11 11 0 0 1 0 2a2 2 0 0 1 2-2z" fill="#ff7f00"/></svg><span>Phone: 555-014-2739</span></div>
  <div class="contact-row"><svg width="13" height="10" viewBox="0 0 13 10"><rect width="13" height="10" fill="#ff7f00"/><path d="M0 0l6.5 5L13 0" fill="none" stroke="#f3f3f3" stroke-width="1.2"/></svg><span>Email: Vireo Kinetics LLC@COM</span></div>
</div>
<div class="footer-divider abs" style="left:367px"></div>
<div class="footer-col newsletter abs" style="left:418px;top:1988px;width:270px">
  <h4>Sign Up For Newsletter</h4>
  <p>Get the latest updates on our courses and events:<br>Notify Me</p>
  <div class="field">Enter Name</div>
  <div class="field">Enter Email<div class="subscribe btn">Subscribe</div></div>
</div>
<div class="footer-divider abs" style="left:718px"></div>
<div class="footer-col abs" style="left:772px;top:1988px">
  <h4>Quick Links</h4>
  <ul class="links"><li>Home</li><li>Services</li><li>Physical Therapy</li><li>Personal Training</li><li>Nutrition</li><li>Contact us</li></ul>
</div>
<div class="footer-divider abs" style="left:925px"></div>
<div class="footer-col abs" style="left:974px;top:1988px">
  <h4>Follow Us</h4>
  <ul class="social"><li><span><i></i></span>Facelink</li><li><span><i></i></span>Chirper</li><li><span><i></i></span>Globe Plus</li><li><span><i></i></span>Linkhub</li></ul>
</div>

<div class="copyright abs">Copyrights &copy; Vireo Kinetics LLC . 2017 | Allrights Reserved.</div>

</body>
</html>
```